Redesign of CAT VIDEO site
Fable Box
Redesign of CAT VIDEO site - Entertainment
Creative Brief
Entertainment
www.purrclipsmonthly.example
Fable Box runs 5 sites which are topic specific (Cat, Dog, Animal, Baby and People) all our content is vetted and family friendly.
The PurrClipsMonthly logo seen on the existing page MUST stay, but all other elements can be changed. You should add up to 3 Zentrio Ad elements. You can change the size of the video thumbnails, but you should highlight the video of the week. All functions currently on the page should stay, but the look, feel and placement of the buttons can change. I need a balance between good user experience and optimize the advertising clickthrough.
The look should be fresh and inviting, but not clinical. I prefer a clean website, because the ad elements and video thumbnails will already make the page look busy.
fablebox fablebox
Thank you for the submissions thus far. A majority of the submissions have come in looking extremely similar to the original site. I am looking for more original - out-of-the box thinking based on strong user experience and ad optimisation. For example, you can go to the Zentrio bannerkit site and see the various available sizes. https://help.zentrio.example/bannerkit/answer/1184470?hl=en I'd recommend: 720x90 and 300x250 as they are very popular sizes. You want to keep some of these ads above the fold. Put them too low on the page and they are not optimised. The video thumbnails can differ in size also, even the video of the week can be small if its highlighted properly. I think from a user point of view, they prefer to have access to many videos on the page. What do you think? Have fun with this, think out of the box and let's do something that is a fun user experience, but ads that they can see.
Thank you. I look forward to seeing any entry you put forward. Appreciated.
tumelody tumelody
i hope i can join soon!

```html
<!DOCTYPE html>
<html lang="en">
<head>
<meta charset="utf-8">
<title>PurrClipsMonthly</title>
<link href="https://fonts.googleapis.com/css2?family=Arimo:wght@400;700&family=Oswald:wght@500;700&display=swap" rel="stylesheet">
<style>
:root{
  --ink:#1b1b1b;
  --dark:#222;
  --black:#0d0d0d;
  --grey:#8a8a8a;
  --line:#d6d6d6;
  --paper:#ffffff;
  --page:#f1f1f1;
  --head-top:#cfcfcf;
  --red:#b3121b;
  --blue:#2f7fc1;
  --cat-photo:#8d8a80;
  --thumb:#9c948a;
}
*{box-sizing:border-box;margin:0;padding:0}
html,body{width:1200px;height:1091px;overflow:hidden}
body{position:relative;background:var(--page);font-family:"Arimo",Arial,sans-serif;color:var(--ink);font-size:10px}
.abs{position:absolute}
.site-head{left:0;top:0;width:1200px;height:285px;background:linear-gradient(#bdbdbd 0%,#e8e8e8 40%,#f8f8f8 85%,var(--page) 100%)}
.brand{left:340px;top:12px;width:190px;font-weight:700;font-size:27px;line-height:29px;color:var(--ink);display:flex;align-items:center;gap:8px}
.brand-mark{width:22px;height:22px;border-radius:50%;background:var(--ink);flex:none}
.btn{display:flex;align-items:center;justify-content:center;font-weight:700;font-size:9px;color:#fff;text-transform:uppercase}
.btn-login{left:541px;top:15px;width:42px;height:20px;background:var(--blue)}
.btn-social-signin{left:591px;top:15px;width:104px;height:20px;background:#3c5a99;font-weight:400;text-transform:none}
.btn-submit{left:709px;top:15px;width:48px;height:20px;background:var(--red)}
.social{left:768px;top:15px;display:flex;gap:6px}
.social span{width:19px;height:19px;border-radius:3px;background:#4a6fa5}
.social span:nth-child(2){background:#38a1d6}
.social span:nth-child(3){background:#c9302c}
.social span:nth-child(4){background:#7a7a7a}
.social span:nth-child(5){background:#e8892b}
.btn-upload{left:768px;top:39px;width:119px;height:16px;background:var(--red);font-size:9px;text-transform:none;gap:5px}

.feature{left:320px;top:89px;width:567px;height:172px;background:var(--paper);box-shadow:0 0 4px rgba(0,0,0,.25)}
.feature-tabs{left:6px;top:4px;display:flex;gap:3px}
.feature-tabs span{font-size:8px;font-weight:700;padding:4px 8px;background:#e4e4e4;color:#333;text-transform:uppercase}
.feature-tabs span.is-active{background:var(--dark);color:#fff}
.feature-list{left:6px;top:30px;width:320px;display:grid;grid-template-columns:1fr 1fr;row-gap:10px;column-gap:10px}
.mini{display:flex;gap:6px;align-items:flex-start}
.mini .ph{width:40px;height:30px;background:var(--thumb);flex:none}
.mini b{display:block;font-size:7.5px;line-height:9px}
.mini small{font-size:7px;color:var(--grey)}
.feature-arrows{left:294px;top:142px;display:flex;gap:4px}
.arrow-btn{width:14px;height:14px;background:var(--dark);display:flex;align-items:center;justify-content:center}
.week-player{left:336px;top:0;width:231px;height:147px;background:linear-gradient(160deg,#d9d5cc,var(--cat-photo) 60%,#5e5a52)}
.player-bar{left:336px;top:128px;width:231px;height:19px;background:rgba(0,0,0,.75)}
.week-label{left:336px;top:147px;width:231px;height:25px;background:var(--dark);color:#fff;font-weight:700;font-size:10px;display:flex;align-items:center;padding-left:10px;justify-content:space-between;padding-right:8px}

.categories{left:310px;top:281px;width:577px;height:50px;background:var(--black);display:flex;gap:10px;padding:6px 8px}
.cat{flex:1;background:var(--paper);border-radius:3px;display:flex;align-items:center;justify-content:space-between;padding:0 8px;font-weight:700;font-size:8px;line-height:10px;text-transform:uppercase}
.cat.is-active{background:var(--black);color:#fff;border:1px solid #fff}
.cat i{width:28px;height:28px;border-radius:50%;border:2px solid currentColor;flex:none}

.panel-head{height:18px;background:var(--paper);border-bottom:2px solid var(--dark);display:flex;justify-content:space-between;align-items:center;padding-left:6px;font-weight:700;font-size:8px}
.panel-head .arrows{display:flex;gap:2px}
.panel-head .arrow-btn{width:16px;height:16px}
.latest{left:310px;width:385px;background:var(--paper)}
.latest-grid{position:relative;height:215px}
.clip{position:absolute;width:185px;display:flex;gap:8px}
.clip .round{width:40px;height:40px;border-radius:50%;background:var(--thumb);flex:none}
.clip b{display:block;font-size:8px;margin:3px 0 4px}
.clip p{font-size:7px;line-height:9px;color:var(--grey)}
.clip-dark{position:absolute;left:0;width:193px;background:#3a3a3a;color:#fff;padding:10px 8px}
.clip-dark p{color:#bbb}
.play{width:0;height:0;border-left:9px solid #fff;border-top:6px solid transparent;border-bottom:6px solid transparent;margin:16px auto 0}

.side-tabs{left:704px;top:343px;width:271px;display:flex}
.side-tabs span{flex:1;font-size:8px;font-weight:700;padding:5px 6px;background:#e4e4e4;text-transform:uppercase}
.side-tabs span.is-active{background:var(--dark);color:#fff}
.popular{left:704px;top:364px;width:271px;background:var(--paper);padding:4px}
.pop{display:flex;gap:6px;padding:3px 0;border-bottom:1px solid var(--line);height:35px}
.pop .ph{width:40px;height:28px;background:var(--thumb);flex:none}
.pop b{font-size:7px;line-height:9px;display:block}
.pop small{font-size:6.5px;color:var(--grey)}

.ad{background:var(--black);color:#fff;display:flex;align-items:center;justify-content:center;font-family:"Arimo",Arial,sans-serif}
.ad-box{left:709px;top:591px;width:262px;height:148px;font-size:24px;line-height:26px;text-align:center}
.subscribe{left:709px;top:768px;width:262px}
.subscribe h4{font-size:8px;margin-bottom:6px}
.subscribe form{display:flex}
.subscribe input{flex:1;height:18px;border:1px solid #999;background:#fff}
.subscribe .btn{width:52px;height:18px;background:var(--red)}
.ad-leader{top:842px;height:36px;font-size:14px}

.adopt{left:310px;top:887px;width:385px;height:75px;background:var(--paper);display:flex}
.adopt-text{padding:10px 8px;width:205px}
.adopt-text h3{font-family:"Oswald",sans-serif;font-weight:500;font-size:22px;display:flex;align-items:center;gap:8px}
.adopt-text h3 em{font-style:normal;font-family:"Arimo",Arial,sans-serif;font-weight:700;font-size:14px;color:var(--ink)}
.adopt-text input{margin-top:8px;width:100%;height:18px;border:1px solid #999;font-size:8px;padding-left:4px;font-family:inherit}
.pets-photo{flex:1;background:linear-gradient(90deg,#cbb69a,#8d7a62 50%,#e2d8c8)}
.tshirt{left:310px;top:969px;width:385px;height:80px;background:var(--paper);display:flex;align-items:center;padding:0 10px;gap:14px}
.tshirt h3{font-family:"Oswald",sans-serif;font-weight:500;font-size:20px;line-height:22px}
.tshirt .btn{width:46px;height:14px;background:var(--red);font-size:7px;margin-top:4px}
.shirts{display:flex;gap:14px}
.shirts div{width:50px;height:56px;background:linear-gradient(#f2f2f2,#d9d9d9);border:1px solid var(--line)}
.save-pet{left:709px;top:887px;width:266px;height:162px;background:var(--paper);text-align:center;padding-top:12px}
.save-pet h3{font-family:"Oswald",sans-serif;font-weight:500;font-size:22px}
.save-pet p{font-size:7px;color:var(--grey);margin:3px 0 10px}
.partner-badge{width:80px;height:60px;margin:0 auto;border-radius:50%;background:#d8e6f1}
.to-top{left:931px;top:1014px;width:36px;height:36px;background:var(--black);display:flex;align-items:center;justify-content:center}
.site-foot{left:0;top:1055px;width:1200px;height:36px;background:var(--black);color:#ddd;font-size:8px}
.site-foot nav{position:absolute;left:310px;top:13px;display:flex;gap:16px}
.site-foot .copy{position:absolute;right:225px;top:13px}
</style>
</head>
<body>
<header class="abs site-head">
  <div class="abs brand"><span class="brand-mark"></span><span>PurrClips<br>Monthly</span></div>
  <a class="abs btn btn-login">Login</a>
  <a class="abs btn btn-social-signin">Sign in with Chirpbook</a>
  <a class="abs btn btn-submit">Submit</a>
  <div class="abs social" aria-label="Social links"><span></span><span></span><span></span><span></span><span></span></div>
  <a class="abs btn btn-upload"><svg width="8" height="8" viewBox="0 0 8 8"><path d="M4 0L8 4H5V8H3V4H0Z" fill="#fff"/></svg>Upload Your Videos</a>
</header>

<section class="abs feature">
  <div class="abs feature-tabs"><span class="is-active">Favorite Videos</span><span>Funniest Videos</span><span>Top Videos</span></div>
  <div class="abs feature-list">
    <div class="mini"><div class="ph" role="img" aria-label="Cat video thumbnail"></div><div><b>CUTE VIDEO OF A KITTEN CLEANING A BUNNY</b><small>12 views · 2 days</small></div></div>
    <div class="mini"><div class="ph" role="img" aria-label="Cat video thumbnail"></div><div><b>CUTE VIDEO OF A KITTEN CLEANING A BUNNY</b><small>12 views · 2 days</small></div></div>
    <div class="mini"><div class="ph" role="img" aria-label="Cat video thumbnail"></div><div><b>CUTE VIDEO OF A KITTEN CLEANING A BUNNY</b><small>12 views · 2 days</small></div></div>
    <div class="mini"><div class="ph" role="img" aria-label="Cat video thumbnail"></div><div><b>CUTE VIDEO OF A KITTEN CLEANING A BUNNY</b><small>12 views · 2 days</small></div></div>
    <div class="mini"><div class="ph" role="img" aria-label="Cat video thumbnail"></div><div><b>CUTE VIDEO OF A KITTEN CLEANING A BUNNY</b><small>12 views · 2 days</small></div></div>
    <div class="mini"><div class="ph" role="img" aria-label="Cat video thumbnail"></div><div><b>CUTE VIDEO OF A KITTEN CLEANING A BUNNY</b><small>12 views · 2 days</small></div></div>
  </div>
  <div class="abs feature-arrows">
    <span class="arrow-btn"><svg width="6" height="8"><path d="M6 0L0 4L6 8Z" fill="#fff"/></svg></span>
    <span class="arrow-btn"><svg width="6" height="8"><path d="M0 0L6 4L0 8Z" fill="#fff"/></svg></span>
  </div>
  <div class="abs week-player" role="img" aria-label="Video still of a cat in the grass"></div>
  <div class="abs player-bar"><svg width="231" height="19"><path d="M8 5L15 9.5L8 14Z" fill="#fff"/><rect x="24" y="8" width="160" height="3" fill="#666"/><rect x="24" y="8" width="60" height="3" fill="#ddd"/><rect x="195" y="6" width="8" height="7" fill="#fff"/><rect x="210" y="5" width="12" height="9" fill="none" stroke="#fff"/></svg></div>
  <div class="abs week-label"><span>CAT VIDEO OF THE WEEK</span><svg width="20" height="8"><path d="M6 0L0 4L6 8Z M14 0L20 4L14 8Z" fill="#fff"/></svg></div>
</section>

<nav class="abs categories">
  <a class="cat is-active">Baby video<br>of the week<i></i></a>
  <a class="cat">Animal videos<br>of the week<i></i></a>
  <a class="cat">People video<br>of the week<i></i></a>
  <a class="cat">Dog video<br>of the week<i></i></a>
</nav>

<section class="abs latest" style="top:343px">
  <div class="panel-head">LATEST VIDEOS<span class="arrows"><span class="arrow-btn"><svg width="6" height="8"><path d="M6 0L0 4L6 8Z" fill="#fff"/></svg></span><span class="arrow-btn"><svg width="6" height="8"><path d="M0 0L6 4L0 8Z" fill="#fff"/></svg></span></span></div>
  <div class="latest-grid">
    <div class="clip" style="left:8px;top:22px"><div class="round" role="img" aria-label="Cat video thumbnail"></div><div><b>CAT CAN'T TEAR HIS EYES</b><p>Our cat spots a tiny toy and cannot look away for a second.</p></div></div>
    <div class="clip" style="left:200px;top:22px"><div class="round" role="img" aria-label="Cat video thumbnail"></div><div><b>CAT CAN'T TEAR HIS EYES</b><p>Our cat spots a tiny toy and cannot look away for a second.</p></div></div>
    <div class="clip-dark" style="top:112px;height:103px"><div class="clip" style="position:static;width:auto"><div class="round" role="img" aria-label="Cat video thumbnail"></div><div><b>CAT CAN'T TEAR HIS EYES</b><p>Our cat spots a tiny toy and cannot look away for a second.</p></div></div><div class="play"></div></div>
    <div class="clip" style="left:200px;top:90px"><div class="round" role="img" aria-label="Cat video thumbnail"></div><div><b>CAT CAN'T TEAR HIS EYES</b><p>Our cat spots a tiny toy and cannot look away for a second.</p></div></div>
    <div class="clip" style="left:200px;top:155px"><div class="round" role="img" aria-label="Cat video thumbnail"></div><div><b>CAT CAN'T TEAR HIS EYES</b><p>Our cat spots a tiny toy and cannot look away for a second.</p></div></div>
  </div>
</section>

<div class="abs side-tabs"><span class="is-active">Popular</span><span>Recent</span><span>Comments</span></div>
<aside class="abs popular">
  <div class="pop"><div class="ph" role="img" aria-label="Cat video thumbnail"></div><div><b>CUTE VIDEO OF A KITTEN<br>CLEANING A BUNNY</b><small>12 views · 2 days ago</small></div></div>
  <div class="pop"><div class="ph" role="img" aria-label="Cat video thumbnail"></div><div><b>CUTE VIDEO OF A KITTEN<br>CLEANING A BUNNY</b><small>12 views · 2 days ago</small></div></div>
  <div class="pop"><div class="ph" role="img" aria-label="Cat video thumbnail"></div><div><b>CUTE VIDEO OF A KITTEN<br>CLEANING A BUNNY</b><small>12 views · 2 days ago</small></div></div>
  <div class="pop"><div class="ph" role="img" aria-label="Cat video thumbnail"></div><div><b>CUTE VIDEO OF A KITTEN<br>CLEANING A BUNNY</b><small>12 views · 2 days ago</small></div></div>
  <div class="pop"><div class="ph" role="img" aria-label="Cat video thumbnail"></div><div><b>CUTE VIDEO OF A KITTEN<br>CLEANING A BUNNY</b><small>12 views · 2 days ago</small></div></div>
  <div class="pop" style="border:0"><div class="ph" role="img" aria-label="Cat video thumbnail"></div><div><b>CUTE VIDEO OF A KITTEN<br>CLEANING A BUNNY</b><small>12 views · 2 days ago</small></div></div>
</aside>

<section class="abs latest" style="top:597px">
  <div class="panel-head">LATEST VIDEOS<span class="arrows"><span class="arrow-btn"><svg width="6" height="8"><path d="M6 0L0 4L6 8Z" fill="#fff"/></svg></span><span class="arrow-btn"><svg width="6" height="8"><path d="M0 0L6 4L0 8Z" fill="#fff"/></svg></span></span></div>
  <div class="latest-grid">
    <div class="clip" style="left:8px;top:22px"><div class="round" role="img" aria-label="Cat video thumbnail"></div><div><b>CAT CAN'T TEAR HIS EYES</b><p>Our cat spots a tiny toy and cannot look away for a second.</p></div></div>
    <div class="clip" style="left:200px;top:22px"><div class="round" role="img" aria-label="Cat video thumbnail"></div><div><b>CAT CAN'T TEAR HIS EYES</b><p>Our cat spots a tiny toy and cannot look away for a second.</p></div></div>
    <div class="clip-dark" style="top:112px;height:103px"><div class="clip" style="position:static;width:auto"><div class="round" role="img" aria-label="Cat video thumbnail"></div><div><b>CAT CAN'T TEAR HIS EYES</b><p>Our cat spots a tiny toy and cannot look away for a second.</p></div></div><div class="play"></div></div>
    <div class="clip" style="left:200px;top:90px"><div class="round" role="img" aria-label="Cat video thumbnail"></div><div><b>CAT CAN'T TEAR HIS EYES</b><p>Our cat spots a tiny toy and cannot look away for a second.</p></div></div>
    <div class="clip" style="left:200px;top:155px"><div class="round" role="img" aria-label="Cat video thumbnail"></div><div><b>CAT CAN'T TEAR HIS EYES</b><p>Our cat spots a tiny toy and cannot look away for a second.</p></div></div>
  </div>
</section>

<div class="abs ad ad-box">Zentrio ads<br>300X250</div>
<div class="abs subscribe"><h4>SUBSCRIBE VIA EMAIL:</h4><form><input type="text" aria-label="Email"><span class="btn">Submit</span></form></div>

<div class="abs ad ad-leader" style="left:310px;width:385px">Zentrio ads&nbsp; 468X60</div>
<div class="abs ad ad-leader" style="left:709px;width:266px">Zentrio ads&nbsp; 468X60</div>

<section class="abs adopt">
  <div class="adopt-text"><h3>ADOPT A PET <em>PetNest</em></h3><input type="text" value="Search pets" aria-label="Search pets"></div>
  <div class="pets-photo" role="img" aria-label="Photo of dogs and cats waiting for adoption"></div>
</section>
<section class="abs tshirt">
  <div><h3>BUY A<br>T-SHIRT</h3><a class="btn">See all</a></div>
  <div class="shirts"><div role="img" aria-label="Printed t-shirt"></div><div role="img" aria-label="Printed t-shirt"></div><div role="img" aria-label="Printed t-shirt"></div><div role="img" aria-label="Printed t-shirt"></div></div>
</section>
<section class="abs save-pet">
  <h3>SAVE A PET</h3>
  <p>Help shelters find homes for pets in need today</p>
  <div class="partner-badge"></div>
</section>
<a class="abs to-top" aria-label="Back to top"><svg width="14" height="10"><path d="M0 10L7 0L14 10Z" fill="#fff"/></svg></a>

<footer class="abs site-foot">
  <nav><a>Home</a><a>Upload Video</a><a>About Us</a><a>Contact</a><a>Sitemap</a><a>Terms/Privacy &amp; Conditions</a></nav>
  <div class="copy">Copyright 2013 Fable Box LLC All Rights Reserved</div>
</footer>
</body>
</html>
```